Ridgeway Auto Care
Ridgeway Auto Care - Automotive
Creative Brief
Professional
Dale Morrow
President
4817 Silver Fern Ln Braselton,GA 30519
d.morrow@ridgewayautocare.example
www.ridgewayautocare.example

```html
<!DOCTYPE html>
<html lang="en">
<head>
<meta charset="utf-8">
<title>Ridgeway Auto Care – Stationery Set</title>
<link href="https://fonts.googleapis.com/css2?family=Cinzel:wght@700&family=Open+Sans:wght@400;700&display=swap" rel="stylesheet">
<style>
  :root{
    --red:#c42f29;
    --dark-red:#8f1d1a;
    --gray:#8c8c8c;
    --light-gray:#c9c9c9;
    --board:#b7b7b7;
    --white:#ffffff;
    --ink:#333333;
    --black:#1e1e1e;
    --faint:#f6dcda;
  }
  *{box-sizing:border-box;margin:0;padding:0}
  html,body{width:1200px;height:974px;overflow:hidden}
  body{font-family:"Open Sans",Arial,sans-serif;background:var(--red)}
  .board{position:absolute;left:14px;top:14px;width:1172px;height:946px;background:var(--board)}
  .piece{position:absolute;overflow:hidden;background:var(--red);box-shadow:0 1px 3px rgba(0,0,0,.25)}
  .piece.white{background:var(--white)}
  .wave{position:absolute;left:0;bottom:0;width:100%}
  .brand{font-family:"Cinzel",Georgia,serif;font-weight:700;color:var(--white);text-align:center;line-height:1.05;letter-spacing:.04em}
  .brand.red{color:var(--red)}
  .fine{position:absolute;color:var(--white);font-size:5px;line-height:1.5}
  .fine.dark{color:var(--ink)}
  .fine b{font-weight:700}
  .mark-circle{position:absolute;border-radius:50%;background:var(--faint)}

  /* top-right brand lockup */
  .lockup{position:absolute;left:900px;top:120px;width:210px;font-size:26px}
  .lockup .sub{font-size:17px}

  /* fax sheet */
  .fax-title{position:absolute;left:16px;top:44px;font:700 24px "Open Sans",Arial,sans-serif;color:var(--black)}
  .fax-fields{position:absolute;left:16px;top:86px;width:246px;display:grid;grid-template-columns:1fr 1fr;column-gap:14px;row-gap:6px}
  .fax-fields span{font-size:6px;color:var(--ink);border-bottom:1px solid var(--light-gray);padding-bottom:2px}
  .fax-checks{position:absolute;left:16px;top:150px;display:flex;gap:8px;font-size:5px;color:var(--ink)}
  .fax-checks span::before{content:"";display:inline-block;width:4px;height:4px;border:1px solid var(--ink);margin-right:2px;vertical-align:-1px}
</style>
</head>
<body>
<svg width="0" height="0" style="position:absolute" aria-hidden="true">
  <defs>
    <symbol id="wave" viewBox="0 0 200 60" preserveAspectRatio="none">
      <rect width="200" height="60" style="fill:var(--white)"/>
      <path d="M0 0H200V18C140 46 70 6 0 26Z" style="fill:var(--red)"/>
      <path d="M0 26C70 6 140 46 200 18V22C140 50 70 10 0 30Z" style="fill:var(--dark-red)"/>
      <path d="M0 30C70 10 140 50 200 22V34C150 58 70 22 0 44Z" style="fill:var(--gray)"/>
    </symbol>
    <symbol id="foot" viewBox="0 0 200 60" preserveAspectRatio="none">
      <path d="M0 34C70 10 140 50 200 20V60H0Z" style="fill:var(--light-gray)"/>
      <path d="M0 40C70 18 140 56 200 28V60H0Z" style="fill:var(--gray)"/>
      <path d="M0 50C70 30 140 62 200 42V60H0Z" style="fill:var(--white)"/>
    </symbol>
  </defs>
</svg>

<main class="board">

  <!-- business card front -->
  <section class="piece" style="left:60px;top:57px;width:176px;height:108px">
    <p class="fine" style="left:10px;top:8px"><b>Dale Morrow</b><br>President</p>
    <p class="brand" style="position:absolute;left:96px;top:26px;width:74px;font-size:9px">Ridgeway<br>Auto Care</p>
    <svg class="wave" height="48" aria-hidden="true"><use href="#wave"/></svg>
  </section>

  <!-- business card back -->
  <section class="piece" style="left:60px;top:189px;width:176px;height:105px">
    <p class="fine" style="left:10px;top:10px">4817 Silver Fern Ln Braselton,GA 30519<br>d.morrow@ridgewayautocare.example<br>www.ridgewayautocare.example</p>
    <svg class="wave" height="46" aria-hidden="true"><use href="#wave"/></svg>
  </section>

  <!-- white card -->
  <section class="piece white" style="left:60px;top:315px;width:176px;height:105px">
    <p class="brand red" style="position:absolute;left:0;top:38px;width:176px;font-size:11px">Ridgeway<br>Auto Care</p>
    <p class="fine dark" style="left:0;top:82px;width:176px;text-align:center">www.ridgewayautocare.example</p>
  </section>

  <!-- letterhead -->
  <section class="piece white" style="left:262px;top:57px;width:263px;height:444px">
    <svg class="wave" style="top:0;bottom:auto" height="50" aria-hidden="true"><use href="#wave"/></svg>
    <p class="fine" style="left:12px;top:6px">Ridgeway Auto Care<br>4817 Silver Fern Ln Braselton,GA 30519</p>
    <div class="mark-circle" style="left:107px;top:196px;width:50px;height:50px"></div>
    <svg class="wave" height="60" aria-hidden="true"><use href="#foot"/></svg>
    <p class="fine dark" style="left:0;bottom:4px;width:263px;text-align:center">www.ridgewayautocare.example</p>
  </section>

  <!-- small card -->
  <section class="piece" style="left:570px;top:57px;width:134px;height:105px">
    <p class="fine" style="left:8px;top:6px">Dale Morrow</p>
    <p class="brand" style="position:absolute;left:0;top:24px;width:134px;font-size:8px">Ridgeway<br>Auto Care</p>
    <svg class="wave" height="46" aria-hidden="true"><use href="#wave"/></svg>
  </section>

  <!-- compliment card -->
  <section class="piece" style="left:570px;top:210px;width:171px;height:92px">
    <p class="fine" style="left:8px;top:8px"><b>Dale Morrow</b><br>President<br>d.morrow@ridgewayautocare.example</p>
    <p class="brand" style="position:absolute;left:108px;top:14px;width:58px;font-size:7px">Ridgeway<br>Auto Care</p>
    <svg class="wave" height="40" aria-hidden="true"><use href="#wave"/></svg>
  </section>

  <!-- envelope front -->
  <section class="piece" style="left:570px;top:307px;width:236px;height:105px">
    <p class="fine" style="left:8px;top:8px">Ridgeway Auto Care<br>4817 Silver Fern Ln</p>
    <p class="brand" style="position:absolute;left:160px;top:16px;width:70px;font-size:8px">Ridgeway<br>Auto Care</p>
    <svg class="wave" height="46" aria-hidden="true"><use href="#wave"/></svg>
  </section>

  <!-- brand lockup -->
  <p class="brand red lockup">RIDGEWAY<br><span class="sub">AUTO CARE</span></p>

  <!-- envelope backs -->
  <svg style="position:absolute;left:841px;top:244px" width="278" height="192" viewBox="0 0 278 192" aria-hidden="true">
    <rect x="0" y="0" width="276" height="110" style="fill:var(--white)"/>
    <path d="M0 0H276L244 34H32Z" style="fill:var(--red)"/>
    <circle cx="138" cy="18" r="6" style="fill:var(--white)"/>
    <rect x="0" y="36" width="276" height="110" style="fill:var(--white)"/>
    <path d="M0 36H276L244 70H32Z" style="fill:var(--black)"/>
    <circle cx="138" cy="54" r="6" style="fill:var(--white)"/>
    <rect x="0" y="72" width="276" height="118" style="fill:var(--white)"/>
    <path d="M0 72H276L244 106H32Z" style="fill:var(--gray)"/>
    <circle cx="138" cy="90" r="6" style="fill:var(--white)"/>
    <text x="220" y="182" style="font:4px 'Open Sans',sans-serif;fill:var(--ink)">www.ridgewayautocare.example</text>
  </svg>

  <!-- presentation folder -->
  <svg style="position:absolute;left:60px;top:486px" width="510" height="394" viewBox="0 0 510 394" aria-label="Presentation folder">
    <path d="M0 20H510V300L490 394H320L305 340H205L190 394H20L0 300Z" style="fill:var(--white)"/>
    <rect x="14" y="0" width="482" height="260" style="fill:var(--red)"/>
    <svg x="14" y="230" width="482" height="70" viewBox="0 0 200 60" preserveAspectRatio="none"><use href="#wave"/></svg>
    <circle cx="118" cy="150" r="22" style="fill:var(--dark-red);opacity:.5"/>
    <text x="380" y="150" text-anchor="middle" style="font:700 24px Cinzel,serif;fill:var(--white)">RIDGEWAY</text>
    <text x="380" y="172" text-anchor="middle" style="font:700 16px Cinzel,serif;fill:var(--white)">AUTO CARE</text>
    <text x="180" y="22" style="font:5px 'Open Sans',sans-serif;fill:var(--white)">Ridgeway Auto Care</text>
    <text x="180" y="29" style="font:5px 'Open Sans',sans-serif;fill:var(--white)">4817 Silver Fern Ln Braselton,GA 30519</text>
    <path d="M20 300H490M205 340L190 394M305 340L320 394" style="stroke:var(--light-gray);fill:none"/>
    <rect x="300" y="312" width="70" height="40" rx="4" style="fill:var(--red)"/>
    <svg x="300" y="332" width="70" height="20" viewBox="0 0 200 60" preserveAspectRatio="none"><use href="#wave"/></svg>
  </svg>

  <!-- CD -->
  <svg style="position:absolute;left:599px;top:559px" width="118" height="118" viewBox="0 0 118 118" aria-label="CD label">
    <clipPath id="disc"><circle cx="59" cy="59" r="58"/></clipPath>
    <g clip-path="url(#disc)">
      <rect width="118" height="118" style="fill:var(--white)"/>
      <svg x="0" y="66" width="118" height="52" viewBox="0 0 200 60" preserveAspectRatio="none"><use href="#foot"/></svg>
    </g>
    <circle cx="59" cy="59" r="58" style="fill:none;stroke:var(--light-gray)"/>
    <text x="59" y="30" text-anchor="middle" style="font:700 8px Cinzel,serif;fill:var(--red)">RIDGEWAY</text>
    <circle cx="59" cy="59" r="12" style="fill:var(--light-gray)"/>
    <circle cx="59" cy="59" r="5" style="fill:var(--board)"/>
  </svg>

  <!-- CD sleeve -->
  <section class="piece" style="left:586px;top:691px;width:155px;height:197px">
    <svg style="position:absolute;left:52px;top:-26px" width="52" height="52" aria-hidden="true"><circle cx="26" cy="26" r="25" style="fill:var(--board)"/></svg>
    <p class="brand" style="position:absolute;left:0;top:70px;width:155px;font-size:12px">RIDGEWAY<br>AUTO CARE</p>
    <svg class="wave" height="70" aria-hidden="true"><use href="#wave"/></svg>
  </section>

  <!-- fax sheet -->
  <section class="piece white" style="left:807px;top:591px;width:279px;height:297px">
    <div style="position:absolute;left:0;top:0;width:100%;height:28px;background:var(--red)"></div>
    <p class="fine" style="left:12px;top:6px">Ridgeway Auto Care<br>4817 Silver Fern Ln Braselton,GA 30519</p>
    <h1 class="fax-title">Fax</h1>
    <div class="fax-fields">
      <span>To:</span><span>From:</span>
      <span>Fax:</span><span>Pages:</span>
      <span>Phone:</span><span>Date:</span>
      <span>Re:</span><span>CC:</span>
    </div>
    <div class="fax-checks"><span>Urgent</span><span>For Review</span><span>Please Comment</span><span>Please Reply</span><span>Please Recycle</span></div>
    <svg class="wave" height="50" aria-hidden="true"><use href="#foot"/></svg>
  </section>

</main>
</body>
</html>
```